Premium Gold Vodka Label Design

English ------------------- We need a label for a Vodka Bottle. Its a sparkling premium vodka with gold inside. The design should look premium. We tried it on our selves but it looks horrible. Therefore we need your help. The current name is corvelle K, but we are open for any better suggestion. We attached the selfmade design. The label will be printed on the bottle. We have other design jobs for you (logo, other sorts)! English ------------------------ We need a label for a vodka bottle. This is a premium vodka which is offset with gold. The design should look like this. We have tried so far and failed. That is why we need your support. The name is so far corvelle K. If you have better suggestions we would be pleased about other suggestions / ideas. In the appendix the failed design is stored. The label is to be applied by screen printing. In the case of good work follow-up projects are guaranteed (logo, other varieties, etc)!
Updates

Reason: We need more time for the decision.

Target Market(s)

USA

Colors

Designer to choose colors to be used in the design.

Requirements
Must have
• English ------------------------ The needed text is on our selfmade label that is attached. English ------------------------ The required texts are stored in the attached design.
Nice to have
• English ------------------------ Transparent places are allowed because we want to print the label on the bottom. English ------------------------ As the label is applied by screen printing, transparent areas are also possible.

```html
<!DOCTYPE html>
<html lang="en">
<head>
<meta charset="utf-8">
<title>Corvelle K Vodka Label</title>
<link rel="stylesheet" href="https://fonts.googleapis.com/css2?family=Tinos:wght@400;700&display=swap">
<style>
  :root {
    --page: #ffffff;
    --label-black: #060606;
    --damask-tone: #1e1e1e;
    --gold: #d9b04c;
    --gold-light: #f3d77a;
    --gold-dark: #a87d22;
    --ivory: #ffffff;
  }
  * { margin: 0; padding: 0; box-sizing: border-box; }
  html, body {
    width: 1200px;
    height: 1000px;
    overflow: hidden;
    background: var(--page);
  }
  .canvas {
    position: relative;
    width: 1200px;
    height: 1000px;
    background: var(--page);
  }
  .label {
    position: absolute;
    left: 303px;
    top: 102px;
    width: 594px;
    height: 795px;
    background: var(--label-black);
    font-family: "Tinos", "Times New Roman", serif;
    color: var(--ivory);
    text-align: center;
  }
  .label__damask {
    position: absolute;
    inset: 0;
    background:
      radial-gradient(ellipse at 50% 35%, #262626 0%, transparent 60%),
      radial-gradient(ellipse at 30% 75%, var(--damask-tone) 0%, transparent 55%),
      radial-gradient(ellipse at 75% 70%, var(--damask-tone) 0%, transparent 55%),
      var(--label-black);
  }
  .label__frame {
    position: absolute;
    left: 26px;
    top: 22px;
    width: 542px;
    height: 740px;
  }
  .label__text {
    position: absolute;
    left: 0;
    width: 100%;
    line-height: 1;
    white-space: nowrap;
  }
  .brand-name {
    top: 190px;
    font-size: 66px;
    letter-spacing: 1px;
    color: var(--ivory);
  }
  .karat {
    top: 360px;
    font-size: 46px;
    color: var(--gold);
  }
  .tagline {
    top: 453px;
    font-size: 25px;
    color: var(--ivory);
  }
  .product-type {
    top: 522px;
    font-size: 72px;
    color: var(--gold);
  }
  .process {
    top: 622px;
    font-size: 23px;
  }
  .process .figure {
    color: var(--gold);
    font-size: 32px;
  }
  .origin {
    top: 655px;
    font-size: 23px;
  }
  .specs {
    top: 712px;
    display: flex;
    justify-content: space-between;
    padding: 0 68px;
    font-size: 22px;
  }
</style>
</head>
<body>
<main class="canvas">
  <section class="label" aria-label="Corvelle K vodka bottle label">
    <div class="label__damask" role="img" aria-label="Dark damask background pattern in black and charcoal"></div>

    <svg class="label__frame" viewBox="0 0 542 740" aria-hidden="true">
      <defs>
        <linearGradient id="gold-leaf" x1="0" y1="0" x2="1" y2="1">
          <stop offset="0" stop-color="#f3d77a"/>
          <stop offset="0.3" stop-color="#c9962f"/>
          <stop offset="0.55" stop-color="#f0cf6a"/>
          <stop offset="0.8" stop-color="#a87d22"/>
          <stop offset="1" stop-color="#e7c25c"/>
        </linearGradient>
      </defs>
      <rect x="6" y="6" width="530" height="728" fill="none" stroke="url(#gold-leaf)" stroke-width="12"/>
    </svg>

    <p class="label__text brand-name">CORVELLE K</p>
    <p class="label__text karat">24kt</p>
    <p class="label__text tagline">PREMIUM GOLD SPARKLING</p>
    <p class="label__text product-type">VODKA</p>
    <p class="label__text process">DISTILLED <span class="figure">8</span> FILTERED</p>
    <p class="label__text origin">MADE IN GERMANY</p>
    <div class="label__text specs">
      <span>40% Alc VOL</span>
      <span>200ml</span>
      <span>80Proof</span>
    </div>
  </section>
</main>
</body>
</html>
```